TKR Advisory Business Cards

Hi there,

I'd like to make a simple new business card design with the logo we already have created for our business.

I need a double sided business card with our logo on the front side and the company and person's details on the back side.

I'd like it to be on a white background and no background so I can potentially use it with either white paper or put it on different coloured paper in accordance with our business colours.

Please use the logo images I have attached and also the fonts.

So Front side:
- Logo in centre of business card (use medium logo so there is a pretty decent border around it, so don't want to fill the whole card but to make it prominent).

Back Side.
- We need 3 different business cards with the different people's name on each.

ie.

Dorian Halvreck
Business Development Manager

m +61 437 206 518
e dorian@tkradvisory.com.au
w tkradvisory.com.au

- Also I'd like to put only the cog/power button logo in the top right hand corner of the card.
(You might need to chop the current logo in half as I don't have a seperate log just for this)
- Also I'd like some lines running on the top left hand corner diagonally, anything that will add to the design or some swirling lines that add some cool effect to the card.

Also I'd like to maybe put our ABN in the bottom right hand corner of the card in a smaller font.

I'd like to also talk to the designer if possible so I can get my idea across a bit better.

Thanks!

Regards,
Dorian

```html
<!DOCTYPE html>
<html lang="en">
<head>
<meta charset="utf-8">
<title>TKR Advisory — Business Cards</title>
<link rel="stylesheet" href="https://fonts.googleapis.com/css2?family=Questrial&display=swap">
<style>
  :root {
    --backdrop: #ecebe8;
    --card-white: #ffffff;
    --charcoal: #4a4a4a;
    --orange: #f39a1d;
    --orange-light: #fbc13a;
    --text-light: #f2f2f2;
    --shadow: rgba(0, 0, 0, 0.22);
  }
  * { margin: 0; padding: 0; box-sizing: border-box; }
  html, body {
    width: 1200px;
    height: 784px;
    overflow: hidden;
    background: var(--backdrop);
    font-family: "Questrial", sans-serif;
  }
  .canvas {
    position: relative;
    width: 1200px;
    height: 784px;
  }
  .card {
    position: absolute;
    width: 600px;
    height: 366px;
    box-shadow: 0 10px 28px var(--shadow);
    overflow: hidden;
  }
  /* Front side */
  .card-front {
    left: 90px;
    top: 60px;
    background: var(--card-white);
    display: flex;
    align-items: center;
    justify-content: center;
  }
  .brand {
    display: flex;
    align-items: center;
    gap: 18px;
  }
  .brand-dot {
    width: 70px;
    height: 70px;
    border-radius: 50%;
    background: var(--charcoal);
  }
  .brand-name {
    font-size: 54px;
    color: var(--charcoal);
    letter-spacing: -0.5px;
  }
  /* Back side */
  .card-back {
    left: 510px;
    top: 340px;
  }
  .card-back-art {
    position: absolute;
    inset: 0;
    width: 100%;
    height: 100%;
  }
  .details {
    position: absolute;
    left: 48px;
    top: 118px;
    color: var(--text-light);
  }
  .person-name {
    font-size: 21px;
    color: var(--orange);
    letter-spacing: 0.3px;
  }
  .person-role {
    font-size: 14px;
    margin-top: 2px;
  }
  .contact-list {
    list-style: none;
    margin-top: 84px;
  }
  .contact-item {
    display: flex;
    align-items: center;
    gap: 9px;
    font-size: 18px;
    line-height: 26px;
  }
  .contact-icon {
    width: 16px;
    height: 16px;
    flex: none;
  }
</style>
</head>
<body>
<main class="canvas">

  <section class="card card-front" aria-label="Business card front">
    <div class="brand">
      <span class="brand-dot"></span>
      <span class="brand-name">TKR Advisory</span>
    </div>
  </section>

  <section class="card card-back" aria-label="Business card back">
    <svg class="card-back-art" viewBox="0 0 600 366" preserveAspectRatio="none" aria-hidden="true">
      <defs>
        <linearGradient id="swoosh-fill" x1="0" y1="0" x2="0" y2="1">
          <stop offset="0" stop-color="var(--orange)"/>
          <stop offset="1" stop-color="var(--orange-light)"/>
        </linearGradient>
      </defs>
      <rect width="600" height="366" fill="var(--charcoal)"/>
      <path d="M318 0 C 300 150, 360 280, 600 300 L600 0 Z" fill="url(#swoosh-fill)"/>
      <path d="M350 0 C 330 150, 390 270, 600 282 L600 0 Z" fill="var(--card-white)"/>
      <circle cx="478" cy="130" r="74" fill="var(--charcoal)"/>
    </svg>

    <div class="details">
      <p class="person-name">Dorian Halvreck</p>
      <p class="person-role">Business Development Manager</p>
      <ul class="contact-list">
        <li class="contact-item">
          <svg class="contact-icon" viewBox="0 0 16 16" aria-hidden="true">
            <path d="M3 1.5 L6 4.5 L4.6 6.4 C5.5 8.3 7.7 10.5 9.6 11.4 L11.5 10 L14.5 13 L12.6 14.8 C7 14.5 1.5 9 1.2 3.4 Z" fill="var(--orange)"/>
          </svg>
          <span>+61 437 206 518</span>
        </li>
        <li class="contact-item">
          <svg class="contact-icon" viewBox="0 0 16 16" aria-hidden="true">
            <rect x="1" y="3" width="14" height="10" rx="1.5" fill="var(--orange)"/>
            <path d="M1.5 4 L8 9 L14.5 4" fill="none" stroke="var(--charcoal)" stroke-width="1.3"/>
          </svg>
          <span>dorian@tkradvisory.com.au</span>
        </li>
        <li class="contact-item">
          <svg class="contact-icon" viewBox="0 0 16 16" aria-hidden="true">
            <circle cx="8" cy="8" r="7" fill="var(--orange)"/>
            <g fill="none" stroke="var(--charcoal)" stroke-width="0.9">
              <ellipse cx="8" cy="8" rx="3" ry="7"/>
              <line x1="1" y1="8" x2="15" y2="8"/>
              <line x1="2.5" y1="4.5" x2="13.5" y2="4.5"/>
              <line x1="2.5" y1="11.5" x2="13.5" y2="11.5"/>
            </g>
          </svg>
          <span>tkradvisory.com.au</span>
        </li>
      </ul>
    </div>
  </section>

</main>
</body>
</html>
```